Open Lantern 5k premium RACE MEDAL

Our annual virtual run is needing a RACE MEDAL to help motivate people to engage with our event. This medal needs to be "bling" that when people see it, they want it. Attached is our event logo.

We particularly like the WAYFARER medal designs which have both front and back. (see https://www.wayfarerquestmedals.com/). It also has a well-branded and premium lanyard/ribbon.

The medal would need to be 6cm x 9cm in size; preferably rectangular with design elements to go beyond the boundaries of the rectangle to premium it up (similar to the wayfarer medals).

The elements to include would be: (1) Open Lantern 5k logo; (2) the words "global running challenge"; (3) the words "LET'S END THIS"; (3) the words "August 2020"; (4) the words "#openlantern5k"; (5) an image of hands that are tied with red ropes (see an example at https://www.pictolunefinder.com/link?src=img&ref=9xQk2LmTr7VbNp4WzHc8&to=https%3A%2F%2Fwww.marrowfieldreaders.org%2Fnotes%2Fshelf-stories%2Fcourtyard-tales%2Fcourtyard-tales-freedom-reading-list&sig=Kq83Zrv1PmTw&t=4820396157).

Some info about the event: we are a charity raising funds to fight human trafficking in Nepal and the Philippines. Our website is openlantern5k.org This medal is awarded only to those that raise a certain amount of funds. It is hoped that having this medal as a reward will motivate people to reach their fundraising goal.

File format needs to be .ai

See more details below in "Must haves" covering the back of the medal.

• The medal design will include front and back (see wayfarerquestmedals.com/ examples). The front is briefed above in the Project Description. For the back, we are thinking of something like a 3D hand (see attached picture - but no red - just metal color), but we are open to other ideas. We also want the following words at the bottom (not in big font - just reasonable enough size to read), "Thanks for caring enough to be one of our top 2020 fundraisers".

```html
<!DOCTYPE html>
<html lang="en">
<head>
<meta charset="utf-8">
<title>Open Lantern 5k — Race Medal, Front and Back</title>
<link rel="stylesheet" href="https://fonts.googleapis.com/css2?family=Bebas+Neue&family=Oswald:wght@500;700&display=swap">
<style>
  :root {
    --stage: #ece8e2;
    --medal-black: #0c0c0c;
    --medal-charcoal: #2a2a2a;
    --gold: #c9a463;
    --gold-light: #f3dfa6;
    --gold-dark: #8a6a32;
    --red: #e41f26;
    --white: #ffffff;
  }
  html, body {
    margin: 0;
    padding: 0;
    width: 1200px;
    height: 813px;
    overflow: hidden;
    background: var(--stage);
  }
  .medal-sheet {
    display: block;
    width: 1200px;
    height: 813px;
  }
  .brand-name {
    font-family: "Bebas Neue", sans-serif;
    fill: var(--white);
    letter-spacing: 1px;
  }
  .event-date {
    font-family: "Bebas Neue", sans-serif;
    fill: var(--gold);
    font-size: 34px;
    letter-spacing: 1px;
  }
  .headline {
    font-family: "Bebas Neue", sans-serif;
    fill: var(--white);
  }
  .headline--red { fill: var(--red); }
  .slogan {
    font-family: "Oswald", sans-serif;
    font-weight: 700;
    font-size: 34px;
    fill: var(--medal-black);
  }
  .hashtag {
    font-family: "Oswald", sans-serif;
    font-weight: 500;
    font-size: 25px;
    fill: var(--gold);
  }
</style>
</head>
<body>
<svg class="medal-sheet" viewBox="0 0 1500 1016" xmlns="http://www.w3.org/2000/svg">
  <defs>
    <radialGradient id="medal-face" cx="0.5" cy="0.45" r="0.6">
      <stop offset="0" stop-color="var(--medal-charcoal)"/>
      <stop offset="1" stop-color="var(--medal-black)"/>
    </radialGradient>
    <linearGradient id="gold-edge" x1="0" y1="0" x2="1" y2="1">
      <stop offset="0" stop-color="var(--gold-dark)"/>
      <stop offset="0.5" stop-color="var(--gold-light)"/>
      <stop offset="1" stop-color="var(--gold-dark)"/>
    </linearGradient>
    <linearGradient id="coin-face" x1="0" y1="0" x2="1" y2="1">
      <stop offset="0" stop-color="#b58d4a"/>
      <stop offset="0.45" stop-color="#f1dba4"/>
      <stop offset="1" stop-color="#a67c3d"/>
    </linearGradient>
    <radialGradient id="bound-hands" cx="0.5" cy="0.45" r="0.6">
      <stop offset="0" stop-color="#9a9a9a"/>
      <stop offset="0.6" stop-color="#4a4a4a"/>
      <stop offset="1" stop-color="#1a1a1a"/>
    </radialGradient>
    <filter id="lift" x="-10%" y="-10%" width="120%" height="120%">
      <feDropShadow dx="4" dy="6" stdDeviation="4" flood-color="#000" flood-opacity="0.5"/>
    </filter>

    <g id="medal-body">
      <polygon points="0,0 479,0 479,718 240,593 0,718" fill="url(#medal-face)" filter="url(#lift)"/>
      <polygon points="19,19 460,19 460,688 240,574 19,688" fill="none" stroke="url(#gold-edge)" stroke-width="5"/>
    </g>

    <g id="slogan-band">
      <polygon points="-26,492 0,465 479,465 505,492 505,585 479,600 0,600 -26,585" fill="var(--red)" filter="url(#lift)"/>
      <rect x="-26" y="528" width="531" height="38" fill="var(--medal-black)"/>
      <text class="slogan" x="240" y="518" text-anchor="middle" transform="skewX(-10) translate(92 0)">LET'S END THIS</text>
      <text class="hashtag" x="240" y="556" text-anchor="middle">#openlantern5k</text>
    </g>
  </defs>

  <!-- Front of medal -->
  <g class="medal medal--front" transform="translate(205 152)">
    <use href="#medal-body"/>

    <g class="brand-lockup">
      <circle cx="112" cy="100" r="14" fill="var(--red)"/>
      <text class="brand-name" x="136" y="116" font-size="50">Open Lantern 5k</text>
    </g>
    <text class="event-date" x="101" y="178">AUGUST 2020</text>

    <rect x="48" y="215" width="130" height="225" rx="40" fill="url(#bound-hands)"
          role="img" aria-label="Photo of clenched hands bound together with red rope"/>
    <rect x="60" y="335" width="110" height="70" rx="20" fill="#9e1b1f" opacity="0.8"/>

    <g class="headline-stack">
      <text class="headline" x="176" y="284" font-size="98">GLOBAL</text>
      <text class="headline headline--red" x="176" y="356" font-size="82">RUNNING</text>
      <text class="headline" x="176" y="420" font-size="70">CHALLENGE</text>
    </g>

    <use href="#slogan-band"/>
  </g>

  <!-- Back of medal -->
  <g class="medal medal--back" transform="translate(808 152)">
    <use href="#medal-body"/>

    <g class="brand-lockup">
      <circle cx="140" cy="92" r="10" fill="var(--red)"/>
      <text class="brand-name" x="157" y="104" font-size="36">Open Lantern 5k</text>
    </g>

    <circle cx="237" cy="310" r="143" fill="none" stroke="url(#gold-edge)" stroke-width="8"/>
    <circle cx="237" cy="310" r="127" fill="url(#coin-face)"
            role="img" aria-label="Embossed metallic handprint on a gold coin"/>

    <use href="#slogan-band"/>
  </g>
</svg>
</body>
</html>
```